Indoor Air Restoration company needs graphic design for a 6x12 v nose trailer to wrap

We offer mold services, duct cleaning, water damage clean up and odor removal. "We find, fix and prevent mold, odor and allergen problems" is what we want to communicate on this trailer, which is a rolling billboard. We like the blue and orange color themes, as found in our logo. The company name is Brightwell Dwelling Services and the logo is attached below. We'd like to see our message clearly, company name and what we offer. We tend to lean towards white letters on a darker background (blue or orange) but are very open to outside ideas, as we are stuck! Our website is available for reference if that is helpful. www.brightwelldwell.example The phone number to be printed on truck is 302-555-0148, Happy designing!!

Target Market(s)

Home owners

Industry/Entity Type

Indoor Air Quality, Mold Remediation

Font styles to use
Sans Serif

Colors
0054AA
0677BA
7BADD7
CADEEF
E8F1F8
F0912C
F2A743
F7CA91
FBE8D2
FDF5EE

Requirements
Must have
• our message, company name and phone
Nice to have
• services we offer (mold remediation, duct cleaning, water damage and odor removal
Should not have
• cartoon feel

```html
<!DOCTYPE html>
<html lang="en">
<head>
<meta charset="utf-8">
<title>Brightwell Dwelling Services – Trailer Wrap</title>
<link rel="stylesheet" href="https://fonts.googleapis.com/css2?family=Source+Sans+3:wght@600;700;800&display=swap">
<style>
  :root{
    --bg-light:#f4f5f6;
    --bg-dark:#d2d4d6;
    --blue-deep:#0054AA;
    --blue-mid:#0677BA;
    --blue-sky:#5fb3dc;
    --blue-pale:#CADEEF;
    --orange:#F0912C;
    --orange-soft:#F7CA91;
    --orange-light:#f9b97a;
    --amber:#f2bd3e;
    --green:#a6cf55;
    --green-rim:#d9ec8c;
    --navy-text:#1f3a8a;
    --white:#ffffff;
    --tile-shadow:#7b7d80;
    --icon:#2a2a2a;
  }
  html,body{margin:0;padding:0;width:1200px;height:1200px;overflow:hidden}
  body{background:radial-gradient(circle at 50% 45%,var(--bg-light) 0%,var(--bg-dark) 100%);font-family:"Source Sans 3",sans-serif}
  .wrap-art{display:block;width:1200px;height:1200px}
  .service-label{font-family:"Source Sans 3",sans-serif;font-weight:700;font-size:21px;fill:var(--white);letter-spacing:1px}
  .brand-name{font-family:"Source Sans 3",sans-serif;font-weight:800;fill:var(--blue-mid);letter-spacing:1px}
  .phone{font-family:"Source Sans 3",sans-serif;font-weight:800;font-size:128px;fill:var(--white)}
  .tagline{font-family:"Source Sans 3",sans-serif;font-weight:700;font-size:38px;fill:var(--white)}
  .website{font-family:"Source Sans 3",sans-serif;font-weight:600;font-size:31px;fill:var(--navy-text)}
  .message{font-family:"Source Sans 3",sans-serif;font-weight:800;font-size:40px;fill:var(--blue-deep);letter-spacing:0.5px}
</style>
</head>
<body>
<svg class="wrap-art" viewBox="0 0 1500 1500" xmlns="http://www.w3.org/2000/svg">
  <defs>
    <linearGradient id="phoneBand" x1="0" x2="1" y1="0" y2="0">
      <stop offset="0" stop-color="#004f8c"/>
      <stop offset="0.5" stop-color="#0a9bd8"/>
      <stop offset="1" stop-color="#004f8c"/>
    </linearGradient>
  </defs>

  <!-- service fan -->
  <g class="service-fan">
    <g class="segment segment-mold">
      <polygon points="48,772 212,636 362,718 292,942 128,942" fill="#8cd0f2"/>
      <polygon points="66,776 215,654 350,724 284,940 136,940" fill="var(--blue-mid)"/>
    </g>
    <g class="segment segment-duct">
      <polygon points="228,428 440,406 538,572 362,716 230,642" fill="var(--orange-soft)"/>
      <polygon points="240,440 436,420 526,572 360,702 242,634" fill="var(--orange-light)"/>
    </g>
    <g class="segment segment-water">
      <polygon points="452,404 566,250 748,322 748,522 538,572" fill="#fbd3a6"/>
      <polygon points="464,410 570,264 742,330 742,520 540,566" fill="var(--orange)"/>
    </g>
    <g class="segment segment-odor">
      <polygon points="750,322 930,244 1062,408 966,576 750,522" fill="#f8e35a"/>
      <polygon points="756,330 926,258 1050,410 960,566 756,520" fill="var(--amber)"/>
    </g>
    <g class="segment segment-air">
      <polygon points="1030,428 1275,432 1290,636 1125,728 968,576" fill="var(--green-rim)"/>
      <polygon points="1040,438 1262,442 1276,630 1122,716 980,574" fill="var(--green)"/>
    </g>
    <g class="segment segment-humidity">
      <polygon points="1128,726 1295,640 1452,770 1368,942 1205,942" fill="#c9ecfb"/>
      <polygon points="1132,732 1292,656 1436,774 1358,940 1208,940" fill="var(--blue-sky)"/>
    </g>

    <!-- service tiles -->
    <g class="tile" transform="translate(160,792) rotate(-30)">
      <rect x="-62" y="-52" width="124" height="120" rx="18" fill="var(--tile-shadow)"/>
      <rect x="-58" y="-60" width="124" height="120" rx="18" fill="var(--white)"/>
      <circle cx="4" cy="0" r="30" fill="var(--icon)" role="img" aria-label="Mold spore icon"/>
    </g>
    <g class="tile" transform="translate(322,510)">
      <rect x="-70" y="-62" width="124" height="130" rx="18" fill="var(--tile-shadow)"/>
      <rect x="-62" y="-66" width="124" height="130" rx="18" fill="var(--white)"/>
      <circle cx="0" cy="-1" r="30" fill="var(--icon)" role="img" aria-label="Air duct and vent icon"/>
    </g>
    <g class="tile" transform="translate(585,362) rotate(28)">
      <rect x="-66" y="-58" width="124" height="120" rx="18" fill="var(--tile-shadow)"/>
      <rect x="-60" y="-64" width="124" height="120" rx="18" fill="var(--white)"/>
      <circle cx="2" cy="-4" r="30" fill="var(--icon)" role="img" aria-label="Leaking roof icon"/>
    </g>
    <g class="tile" transform="translate(902,362) rotate(-30)">
      <rect x="-58" y="-58" width="124" height="120" rx="18" fill="var(--tile-shadow)"/>
      <rect x="-62" y="-64" width="124" height="120" rx="18" fill="var(--white)"/>
      <circle cx="0" cy="-4" r="30" fill="var(--icon)" role="img" aria-label="Nose and odor icon"/>
    </g>
    <g class="tile" transform="translate(1182,518)">
      <rect x="-56" y="-62" width="128" height="126" rx="18" fill="var(--tile-shadow)"/>
      <rect x="-62" y="-66" width="124" height="126" rx="18" fill="var(--white)"/>
      <circle cx="0" cy="-3" r="30" fill="var(--icon)" role="img" aria-label="House with fan icon"/>
    </g>
    <g class="tile" transform="translate(1340,790) rotate(32)">
      <rect x="-56" y="-56" width="124" height="120" rx="18" fill="var(--tile-shadow)"/>
      <rect x="-62" y="-62" width="124" height="120" rx="18" fill="var(--white)"/>
      <circle cx="0" cy="-2" r="30" fill="var(--icon)" role="img" aria-label="Humidity sensor icon"/>
    </g>

    <!-- service labels -->
    <text class="service-label" transform="translate(248,908) rotate(-80)">MOLD REMEDIATION</text>
    <text class="service-label" transform="translate(336,652) rotate(-50)">DUCT CLEANING</text>
    <text class="service-label" transform="translate(542,488) rotate(-14)">WATER DAMAGE</text>
    <text class="service-label" transform="translate(798,450) rotate(14)">ODOR REMOVAL</text>
    <text class="service-label" transform="translate(1056,556) rotate(44)">AIR QUALITY</text>
    <text class="service-label" transform="translate(1214,718) rotate(76)">HUMIDITY SOLUTION</text>
  </g>

  <!-- central dome -->
  <path class="dome" d="M280,944 C300,700 500,522 745,522 C990,522 1190,700 1206,944 Z" fill="var(--white)"/>

  <!-- brand name -->
  <g class="brand">
    <rect x="704" y="620" width="84" height="84" fill="var(--blue-mid)"/>
    <text class="brand-name" x="745" y="820" text-anchor="middle" font-size="60">BRIGHTWELL DWELLING</text>
    <text class="brand-name" x="745" y="896" text-anchor="middle" font-size="60">SERVICES</text>
  </g>

  <!-- phone band -->
  <polygon class="phone-band" points="60,1012 118,950 1384,950 1442,1012 1384,1086 118,1086" fill="url(#phoneBand)"/>
  <text class="phone" x="750" y="1062" text-anchor="middle">302-555-0148</text>

  <!-- tagline band -->
  <polygon class="tagline-band" points="364,1140 410,1092 1096,1092 1140,1140 1096,1190 410,1190" fill="var(--green)"/>
  <text class="tagline" x="752" y="1136" text-anchor="middle">BRIGHTWELL DWELLING SERVICES</text>
  <text class="tagline" x="752" y="1178" text-anchor="middle">TRUSTED &amp; CERTIFIED</text>

  <!-- website band -->
  <polygon class="web-band" points="470,1224 500,1196 1006,1196 1032,1224 1006,1254 500,1254" fill="var(--amber)"/>
  <text class="website" x="750" y="1235" text-anchor="middle">www.brightwelldwell.example</text>

  <!-- core message -->
  <text class="message" x="750" y="1318" text-anchor="middle">WE FIND, FIX AND PREVENT MOLD, ODOR AND ALLERGEN PROBLEMS</text>
</svg>
</body>
</html>
```